BOND WITH TOBY FOR SPECIALISED ADHESIVE AND SEALANTS.

Details for my new Banner Ad Design Project will be added soon.
All that I am looking for is WORDING that can demonstrate to potential customers what the products can achieve and describing the various materials that this special adhesive will stick and why they need to choose it also a logo or even new name to fit in if financially possible
The size of the banner is unimportant as I only need help in getting the message over then I will adjust accordingly or pay the designer to complete.
As I am very limited in my knowledge of web design in fact it is non existent your help is paramount for the result.
This is a new project for me as I am now a young retired person who is looking for something different to follow.
Please let me know if the information I supply is in sufficient,
Best regards to all and in your design careers.
Updates

As pointed out to me that my request is to broad for a result,but I am not looking for words that describe a space shot, I am looking for suggestions to help me to put together some form of ad that helps me get the business off the ground ,I am no expert in marketing and design, so any format of words would be helpful,thank you all and remember, " you are the experts".

Target Market(s)

General public in the UK,and commercial business.
It would be used where there is a requirement to seal/or stick difficult materials or items but not large items like roofs/buildings etc.

Industry/Entity Type

Adhesive

Font styles to use
Sans Serif

Colors

Designer to choose colors to be used in the design.

Requirements
Must have
• To make people feel they will need the product or service maybe not initially but soon.
Nice to have
• This can be anything related to sticking or sealing different household products,
Should not have
• old fashioned font

```html
<!DOCTYPE html>
<html lang="en">
<head>
<meta charset="utf-8">
<title>Bond With Toby – Special Adhesive Banner</title>
<link rel="stylesheet" href="https://fonts.googleapis.com/css2?family=Montserrat:wght@400;500;600&display=swap">
<style>
  :root {
    --stage: #232426;
    --brand-orange: #fd8142;
    --divider: #f4f6f8;
    --ink: #2c323d;
    --white: #ffffff;
    --photo-light: #d3e7f3;
    --photo-mid: #b8d6ea;
    --photo-deep: #a9cbe2;
  }
  * { margin: 0; padding: 0; box-sizing: border-box; }
  html, body {
    width: 1200px;
    height: 750px;
    overflow: hidden;
    background: var(--stage);
    font-family: "Montserrat", Arial, sans-serif;
  }
  .banner {
    position: absolute;
    left: 5px;
    top: 200px;
    width: 1190px;
    height: 349px;
    display: flex;
  }
  .brand-panel {
    position: relative;
    width: 536px;
    height: 100%;
    background: var(--brand-orange);
    color: var(--white);
    display: flex;
    flex-direction: column;
    justify-content: center;
    padding-left: 66px;
  }
  .divider {
    width: 2px;
    height: 100%;
    background: var(--divider);
  }
  .brand-name {
    font-size: 64px;
    font-weight: 500;
    line-height: 72px;
    letter-spacing: 1px;
  }
  .brand-name span { display: block; }
  .tagline {
    margin-top: 22px;
    font-size: 22px;
    font-weight: 500;
    letter-spacing: 3px;
    line-height: 28px;
  }
  .materials-panel {
    position: relative;
    flex: 1;
    height: 100%;
    overflow: hidden;
  }
  .product-photo {
    position: absolute;
    inset: 0;
    background:
      radial-gradient(ellipse at 85% 35%, var(--photo-light) 0%, transparent 55%),
      linear-gradient(160deg, var(--photo-light) 0%, var(--photo-mid) 55%, var(--photo-deep) 100%);
  }
  .materials {
    position: absolute;
    left: 39px;
    top: 28px;
    color: var(--ink);
  }
  .materials-title {
    font-size: 30px;
    font-weight: 600;
    letter-spacing: 2px;
    line-height: 36px;
    margin-bottom: 8px;
  }
  .materials-list li {
    font-size: 23px;
    font-weight: 400;
    letter-spacing: 1px;
    line-height: 30px;
    list-style: none;
  }
  .materials-more {
    font-size: 20px;
    font-weight: 400;
    letter-spacing: 0.6px;
    line-height: 30px;
  }
</style>
</head>
<body>
  <div class="banner">
    <section class="brand-panel">
      <h1 class="brand-name"><span>BOND WITH</span><span>TOBY</span></h1>
      <p class="tagline">SPECIAL ADHESIVE</p>
    </section>
    <div class="divider"></div>
    <section class="materials-panel">
      <div class="product-photo" role="img" aria-label="Photo of a white glue bottle with an orange nozzle beside a drop of white adhesive on a pale blue surface"></div>
      <div class="materials">
        <h2 class="materials-title">STICKS</h2>
        <ul class="materials-list">
          <li>GLASS</li>
          <li>LEATHER</li>
          <li>WOOD</li>
          <li>STEEL</li>
          <li>CARD</li>
          <li>CLOTH</li>
          <li>ALL PLASTICS</li>
        </ul>
        <p class="materials-more">and much much more....</p>
      </div>
    </section>
  </div>
</body>
</html>
```